Creation of foldable A4 Leaflet to summarise my website

I need to summarize the content of my website into a 4 facecs-2 pages A4 foldable leaflet. I need the leaflet to go through the main topics of my website, with accurate descriptions and some pics taken from the website. Focusing about professionality and over 25 year experience on the field. Give also apace to our valued partners and customers
My website plimborex.au

Target Market(s)

Industrial filtration, dust collector business

Industry/Entity Type

Industrial filtration, dust collectors market, mining, powerplant, cement industry

Font styles to use
Sans Serif

Colors
0054AA
0677BA
7BADD7
CADEEF
E8F1F8

Requirements
Must have
• clear references to my website
Nice to have
• clear and clean layout
Should not have
• dark colours other than blue and navy, as per my logo

```html
<!DOCTYPE html>
<html lang="en">
<head>
<meta charset="utf-8">
<title>Plimborex Trifold Leaflet</title>
<link href="https://fonts.googleapis.com/css2?family=Saira+Condensed:wght@700;800&family=Outfit:wght@400;500;600;700&display=swap" rel="stylesheet">
<style>
:root{
  --navy:#0d2a4f;
  --brand:#0054aa;
  --blue:#0677ba;
  --sky:#7badd7;
  --mist:#cadeef;
  --ice:#e8f1f8;
  --contact-bg:#5a91d3;
  --services-bg:#2f6fb8;
  --supply-bg:#4a88d6;
  --stage:#c9c8ca;
  --white:#ffffff;
  --ink:#1a1a1a;
}
*{margin:0;padding:0;box-sizing:border-box}
html,body{width:911px;height:1200px;overflow:hidden;background:var(--stage)}
.stage{position:relative;width:911px;height:1200px;background:var(--stage);font-family:"Outfit",sans-serif;color:var(--ink)}
.spread{position:absolute;left:113px;width:674px;height:450px;overflow:hidden}
.spread--outer{top:130px}
.spread--inner{top:597px}
.panel{position:absolute;top:0;height:450px;overflow:hidden}
.heading{font-family:"Saira Condensed",sans-serif;font-weight:800;letter-spacing:.3px;line-height:1;position:absolute;white-space:nowrap}
.heading .accent{color:var(--brand)}
.divider{position:absolute;height:8px}
.divider::before{content:"";position:absolute;left:0;right:0;top:3px;height:1.5px;background:currentColor}
.divider::after{content:"";position:absolute;left:50%;top:1px;width:5px;height:5px;margin-left:-2.5px;border-radius:50%;background:currentColor}
.photo{position:absolute}
.photo--round{border-radius:50%}

/* about */
.about{left:0;width:224px;background:var(--white)}
.about .heading{left:20px;top:26px;font-size:21px;color:var(--navy)}
.about .divider{left:19px;top:22+0px;width:49px;top:50px;color:var(--sky)}
.about-sub{position:absolute;left:18px;top:61px;width:200px;font-size:12px;font-weight:600;line-height:15px;color:var(--ink)}
.about-copy{position:absolute;left:18px;top:97px;width:190px;font-size:7.7px;line-height:14.1px;text-align:justify;color:var(--ink)}
.about-art{position:absolute;left:0;top:0}

/* contact */
.contact{left:224px;width:224px;background:var(--contact-bg)}
.contact-art{position:absolute;left:0;top:0}
.contact .heading{left:0;right:0;text-align:center;top:219px;font-size:21px;color:var(--white)}
.contact .divider{left:90px;width:45px;top:244px;color:var(--white)}
.contact-icon{position:absolute;left:101px;width:23px;height:23px;border-radius:50%;background:var(--navy);display:flex;align-items:center;justify-content:center}
.contact-phone{position:absolute;left:0;right:0;top:298px;text-align:center;font-family:"Saira Condensed",sans-serif;font-weight:700;font-size:29px;color:var(--white);line-height:1}
.contact-email{position:absolute;left:0;right:0;top:369px;text-align:center;font-size:12.5px;color:var(--white)}
.contact-social{position:absolute;left:0;right:0;top:440px}

/* cover */
.cover{left:448px;width:226px;background:var(--white)}
.cover-art{position:absolute;left:0;top:0}
.badge{position:absolute;left:15px;top:177px;width:88px;height:88px;border-radius:50%;background:var(--navy);border:3px solid var(--white);color:var(--white);text-align:center;font-family:"Saira Condensed",sans-serif;font-weight:800;display:flex;flex-direction:column;justify-content:center;line-height:1}
.badge-years{font-size:18px}
.badge-label{font-size:12px;margin-top:1px}
.brand{position:absolute;left:21px;top:296px;display:flex;align-items:center;gap:6px}
.brand-mark{width:36px;height:36px;border-radius:50%;background:var(--brand)}
.brand-name{font-size:14px;font-weight:700;color:var(--navy);line-height:1;letter-spacing:.6px}
.brand-tag{font-size:5.6px;font-weight:700;color:var(--brand);letter-spacing:1.4px;line-height:8px;margin-top:2px}
.cover-title{position:absolute;left:0;right:0;text-align:center;font-family:"Saira Condensed",sans-serif;font-weight:800;line-height:1;white-space:nowrap}
.cover-title--1{top:338px;font-size:29px;color:var(--navy)}
.cover-title--2{top:362px;font-size:40px;color:var(--navy)}
.cover-title--3{top:399px;font-size:26px;color:var(--brand)}
.cover-title--4{top:423px;font-size:17.5px;color:var(--brand)}

/* partners & clients */
.partners{left:0;width:226px;background:var(--white)}
.partners-art{position:absolute;left:0;top:0}
.partners .heading{left:0;right:0;text-align:center;font-size:20.5px;color:var(--navy)}
.partners .heading--partners{top:21px}
.partners .heading--clients{top:263px}
.partners .divider{left:83px;width:45px;color:var(--brand)}
.partner-name{position:absolute;left:0;right:0;text-align:center;font-size:15px;font-weight:600;color:#555d66}
.client-grid{position:absolute;left:12px;top:320px;width:206px;display:grid;grid-template-columns:repeat(4,1fr);row-gap:16px;column-gap:4px}
.client{display:flex;align-items:center;justify-content:center;gap:2px;height:18px;font-size:6.6px;font-weight:700;color:var(--navy);text-align:center;line-height:1.05}
.client-dot{width:6px;height:6px;border-radius:50%;background:var(--brand);flex:none}

/* services */
.services{left:226px;width:224px;background:var(--services-bg)}
.supply{left:450px;width:224px;background:var(--supply-bg)}
.services .heading{left:0;right:0;text-align:center;top:9px;font-size:21px;color:var(--white)}
.services .divider{left:88px;width:45px;top:33px;color:var(--white)}
.service{position:absolute;left:0;right:0;text-align:center;color:var(--white)}
.service .photo{left:50%;margin-left:-43px;top:0;width:86px;height:86px;border:2px solid var(--white)}
.service-title{position:absolute;left:0;right:0;top:92px;font-size:12.3px;font-weight:600;white-space:nowrap}
.service-text{position:absolute;left:0;right:0;top:111px;font-size:7.8px}
</style>
</head>
<body>
<main class="stage">

  <!-- Outer spread -->
  <section class="spread spread--outer">

    <div class="panel about">
      <svg class="about-art" width="224" height="450" viewBox="0 0 224 450" aria-hidden="true">
        <path d="M224 200 C190 240 168 300 168 450 L190 450 C188 320 200 260 224 230 Z" fill="var(--mist)"/>
        <path d="M224 250 C205 290 196 360 200 450 L206 450 C202 370 210 300 224 268 Z" fill="var(--sky)"/>
        <path d="M0 278 A125 125 0 0 1 218 450" fill="none" stroke="var(--brand)" stroke-width="4"/>
      </svg>
      <div class="photo" role="img" aria-label="Technicians in white protective suits fitting filter bags inside a dust collector" style="left:0;top:280px;width:210px;height:170px;border-top-right-radius:150px 170px;background:linear-gradient(135deg,#e6e6e6,#8e8e8e 60%,#4a4a4a)"></div>
      <h2 class="heading">ABOUT <span class="accent">US</span></h2>
      <span class="divider"></span>
      <p class="about-sub">The Journey of Environmental Service Excellence</p>
      <p class="about-copy">Originating from a desire to provide more robust technical support to the Australia wide industrial sector, we began our journey by focusing on the critical need for reliable dust management. We recognised that many facilities struggled with maintaining complex filtration systems, and we stepped in to offer a more dedicated, hands-on approach. This foundation allowed us to build a reputation based on technical merit and unwavering support for our clients.</p>
    </div>

    <div class="panel contact">
      <svg class="contact-art" width="224" height="450" viewBox="0 0 224 450" aria-hidden="true">
        <path d="M0 330 C40 200 130 90 224 30 L224 0 C120 60 20 180 0 280 Z" fill="#6a9ddb" opacity=".6"/>
        <circle cx="113" cy="113" r="95" fill="var(--brand)" opacity=".55"/>
      </svg>
      <div class="photo photo--round" role="img" aria-label="Dust collector pulse-jet manifolds with blue headers inside a factory" style="left:25px;top:20px;width:178px;height:178px;border:6px solid var(--white);background:linear-gradient(160deg,#d7d2c4,#a8b3bd 45%,#3f8fd8 70%,#6e6e6e)"></div>
      <h2 class="heading">CONTACT US</h2>
      <span class="divider"></span>
      <span class="contact-icon" style="top:271px">
        <svg width="11" height="11" viewBox="0 0 24 24" aria-hidden="true"><path fill="#fff" d="M6.6 10.8a15 15 0 0 0 6.6 6.6l2.2-2.2c.3-.3.7-.4 1-.2 1.1.4 2.3.6 3.6.6.6 0 1 .4 1 1V20c0 .6-.4 1-1 1A17 17 0 0 1 3 4c0-.6.4-1 1-1h3.5c.6 0 1 .4 1 1 0 1.3.2 2.5.6 3.6.1.3 0 .7-.2 1z"/></svg>
      </span>
      <p class="contact-phone">0400 555 218</p>
      <span class="contact-icon" style="top:344px">
        <svg width="12" height="12" viewBox="0 0 24 24" aria-hidden="true"><path fill="#fff" d="M3 5h18v14H3z"/><path fill="none" stroke="#0d2a4f" stroke-width="1.8" d="M3 5l9 8 9-8"/></svg>
      </span>
      <p class="contact-email">hello@plimborex.au</p>
      <span class="contact-icon" style="top:406px;width:23px"></span>
      <p class="contact-email" style="top:432px;font-size:8px">Linkwise</p>
    </div>

    <div class="panel cover">
      <svg class="cover-art" width="226" height="450" viewBox="0 0 226 450" aria-hidden="true">
        <path d="M0 30 L60 0 L80 0 L0 60 Z" fill="var(--mist)"/>
        <path d="M25 0 A186 186 0 0 0 226 304" fill="none" stroke="var(--brand)" stroke-width="8"/>
        <defs><linearGradient id="coverPhoto" x1="0" y1="0" x2="1" y2="1"><stop offset="0" stop-color="#9aa3ad"/><stop offset=".45" stop-color="#2b57a0"/><stop offset=".8" stop-color="#e9e2cf"/><stop offset="1" stop-color="#d8b860"/></linearGradient></defs>
        <path d="M23 0 L226 0 L226 288 A176 176 0 0 1 23 0 Z" fill="url(#coverPhoto)" role="img" aria-label="Engineer in a hard hat inspecting rolled filter bags beside a baghouse dust collector"/>
      </svg>
      <div class="badge"><span class="badge-years">25 YEAR</span><span class="badge-label">EXPERIENCE</span></div>
      <div class="brand">
        <span class="brand-mark"></span>
        <div>
          <p class="brand-name">PLIMBOREX</p>
          <p class="brand-tag">ENVIRONMENTAL<br>SERVICES</p>
        </div>
      </div>
      <p class="cover-title cover-title--1">PREMIUM DUST</p>
      <p class="cover-title cover-title--2">COLLECTOR</p>
      <p class="cover-title cover-title--3">SUPPLY &amp; EXPERT</p>
      <p class="cover-title cover-title--4">MAINTENANCE SOLUTIONS</p>
    </div>

  </section>

  <!-- Inner spread -->
  <section class="spread spread--inner">

    <div class="panel partners">
      <svg class="partners-art" width="226" height="450" viewBox="0 0 226 450" aria-hidden="true">
        <path d="M0 295 A125 125 0 0 1 226 295 L226 310 A120 120 0 0 0 0 310 Z" fill="var(--brand)"/>
        <path d="M0 290 A126 120 0 0 1 113 176 A126 120 0 0 1 226 290" fill="none" stroke="var(--brand)" stroke-width="9"/>
      </svg>
      <h2 class="heading heading--partners">OUR <span class="accent">PARTNERS</span></h2>
      <span class="divider" style="top:45px"></span>
      <p class="partner-name" style="top:78px">Fennor Filtration</p>
      <p class="partner-name" style="top:121px">Calvetra</p>
      <h2 class="heading heading--clients">OUR <span class="accent">CLIENTS</span></h2>
      <span class="divider" style="top:288px"></span>
      <div class="client-grid">
        <span class="client">Oakvale Brick</span>
        <span class="client">Harbourline Concrete</span>
        <span class="client">Rockpoint Cement</span>
        <span class="client">Southland Cement</span>
        <span class="client">Coastway Cement</span>
        <span class="client">Stonemark</span>
        <span class="client">Ferrolux</span>
        <span class="client">Buildcore</span>
        <span class="client">Golden Field Grains</span>
        <span class="client">Kestrel</span>
        <span class="client">Marlow Plant</span>
        <span class="client">Tarrow</span>
      </div>
    </div>

    <div class="panel services">
      <h2 class="heading">OUR SERVICES</h2>
      <span class="divider"></span>
      <div class="service" style="top:50px">
        <div class="photo photo--round" role="img" aria-label="Tube sheet of a dust collector during servicing" style="background:radial-gradient(circle at 40% 40%,#9aa2aa,#4a5058)"></div>
        <p class="service-title">Dust Collectors Servicing</p>
        <p class="service-text">Industrial maintenance, dust collector repair</p>
      </div>
      <div class="service" style="top:184px">
        <div class="photo photo--round" role="img" aria-label="Close view of filter cells in a dust collector plate" style="background:radial-gradient(circle at 50% 50%,#c8ccc8,#6c7278)"></div>
        <p class="service-title">Dust Collectors Regular Maintenance</p>
        <p class="service-text">Scheduled servicing, system upkeep</p>
      </div>
      <div class="service" style="top:318px">
        <div class="photo photo--round" role="img" aria-label="Worker in high-visibility vest installing filter bags in a baghouse" style="background:linear-gradient(135deg,#8a90b8,#5a5f80 55%,#e8d020 75%,#7a7f9a)"></div>
        <p class="service-title">Filtration Bags Install</p>
        <p class="service-text">Baghouse installation, filter fitting</p>
      </div>
    </div>

    <div class="panel supply">
      <div class="service" style="top:26px">
        <div class="photo photo--round" role="img" aria-label="Industrial filter bags in brown and cream fabrics" style="background:linear-gradient(120deg,#f2f2f2,#c9a27a 50%,#e8dcc6)"></div>
        <p class="service-title">Filtration Bags Supply</p>
        <p class="service-text">Industrial filter bags, dust media</p>
      </div>
      <div class="service" style="top:162px">
        <div class="photo photo--round" role="img" aria-label="Dust collector control timer units" style="background:radial-gradient(circle at 55% 45%,#5a5f66,#d9dadc 70%,#ffffff)"></div>
        <p class="service-title">Dust Collectors Spare Parts Supply</p>
        <p class="service-text">Replacement filters, collector components</p>
      </div>
      <div class="service" style="top:298px">
        <div class="photo photo--round" role="img" aria-label="Large industrial dust collector unit at a plant" style="background:linear-gradient(160deg,#b7b0a2,#8c8f94 50%,#5e6166)"></div>
        <p class="service-title">Dust Collectors Supply</p>
        <p class="service-text">Filtration system units, industrial supply</p>
      </div>
    </div>

  </section>
</main>
</body>
</html>
```